Heritage Hollow Business Cards

Require a business card design. <br/><br/>Needs to include logo (either round or long version) plus these details:<br/>Maya Torvel<br/>Heritage Hollow<br/>maya@quonbrook.com.au<br/>02 6481 7390<br/>PO Box Glenwarra NSW 2913<br/>www.heritagehollow.com.au<br/><br/>I need in an editable format so that I can create for multiple staff members. <br/><br/>

Target Market(s)

We are an online store selling renovation products to home owners are builders. Looking for a classic classy design.

Industry/Entity Type

Home And Garden

Contact Information for Business Card

Maya Torvel
Heritage Hollow
maya@quonbrook.com.au
02 6481 7390
PO Box Glenwarra NSW 2913
www.heritagehollow.com.au

Colors

Designer to choose colors to be used in the design.

Requirements
Must have
• Must include Logo.

```html
<!DOCTYPE html>
<html lang="en">
<head>
<meta charset="utf-8">
<title>Heritage Hollow Business Cards</title>
<link rel="stylesheet" href="https://fonts.googleapis.com/css2?family=Roboto:wght@400;500;700&display=swap">
<style>
  :root {
    --bg: #d9d9d9;
    --green: #44614f;
    --gold: #c9962e;
    --white-card: #f3f3f3;
    --ink: #2d2d2d;
    --accent: #3f5d4b;
    --faint: #e3e3e3;
  }
  * { box-sizing: border-box; margin: 0; padding: 0; }
  html, body { width: 1200px; height: 1021px; overflow: hidden; }
  body {
    background: var(--bg);
    font-family: "Roboto", sans-serif;
    position: relative;
  }
  .card {
    position: absolute;
    width: 700px;
    height: 400px;
    left: 250px;
    box-shadow: 0 10px 28px rgba(0,0,0,0.25);
  }
  .card-back { top: 70px; background: var(--green); }
  .card-front { top: 540px; background: var(--white-card); overflow: hidden; }

  .back-mark {
    position: absolute;
    left: 50%; top: 50%;
    width: 230px; height: 230px;
    transform: translate(-50%, -50%);
    border: 3px solid var(--gold);
    border-radius: 50%;
    display: flex; align-items: center; justify-content: center;
  }
  .back-name {
    color: var(--gold);
    font-weight: 500;
    font-size: 30px;
    line-height: 1.1;
    text-align: center;
  }

  .front-brand {
    position: absolute;
    left: 48px; top: 46px;
    display: flex; align-items: center; gap: 12px;
  }
  .front-brand .dot {
    width: 40px; height: 40px; border: 2px solid var(--ink); border-radius: 50%;
  }
  .front-brand .name {
    font-size: 28px; font-weight: 500; color: var(--ink);
  }
  .rule { position: absolute; left: 48px; width: 40px; height: 2px; background: var(--accent); }
  .rule-1 { top: 128px; }
  .rule-2 { top: 218px; }
  .address {
    position: absolute; left: 48px; top: 146px;
    font-size: 19px; line-height: 1.3; color: var(--ink);
  }
  .contacts {
    position: absolute; left: 48px; top: 236px;
    list-style: none; font-size: 19px; line-height: 1.35; color: var(--ink);
  }
  .contacts li { display: flex; align-items: center; gap: 8px; }
  .contacts svg { width: 16px; height: 16px; flex: none; }
  .person {
    position: absolute; right: 56px; top: 226px; text-align: right;
  }
  .person .full-name {
    font-size: 27px; font-weight: 700; color: var(--accent); letter-spacing: 0.5px;
  }
  .person .role {
    font-size: 17px; font-weight: 500; color: var(--ink); letter-spacing: 0.5px;
  }
  .faint-ring {
    position: absolute; left: 330px; top: 250px;
    width: 300px; height: 300px;
    border: 2px solid var(--faint); border-radius: 50%;
  }
</style>
</head>
<body>
  <section class="card card-back">
    <div class="back-mark">
      <div class="back-name">Heritage<br>Hollow</div>
    </div>
  </section>

  <section class="card card-front">
    <div class="faint-ring"></div>
    <div class="front-brand">
      <span class="dot"></span>
      <span class="name">Heritage Hollow</span>
    </div>
    <span class="rule rule-1"></span>
    <p class="address">PO Box Glenwarra<br>NSW 2913</p>
    <span class="rule rule-2"></span>
    <ul class="contacts">
      <li>
        <svg viewBox="0 0 16 16"><path d="M3 1l3 3-2 2c1 2 3 4 5 5l2-2 3 3-2 3C7 15 1 9 1 3z" fill="var(--accent)"/></svg>
        02 6481 7390
      </li>
      <li>
        <svg viewBox="0 0 16 16"><rect x="1" y="3" width="14" height="10" fill="none" stroke="var(--accent)" stroke-width="1.5"/><path d="M1 3l7 6 7-6" fill="none" stroke="var(--accent)" stroke-width="1.5"/></svg>
        maya@quonbrook.com.au
      </li>
      <li>
        <svg viewBox="0 0 16 16"><circle cx="8" cy="8" r="6.5" fill="none" stroke="var(--accent)" stroke-width="1.5"/><path d="M1.5 8h13M8 1.5c-3 3-3 10 0 13M8 1.5c3 3 3 10 0 13" fill="none" stroke="var(--accent)" stroke-width="1.2"/></svg>
        www.heritagehollow.com.au
      </li>
    </ul>
    <div class="person">
      <div class="full-name">MAYA TORVEL</div>
      <div class="role">OWNER</div>
    </div>
  </section>
</body>
</html>
```